banners,restaurant takeaway menu,catering packages for function room and takeaway

We are running indian restaurant in sydney and want to put feather type flags around our boundary.

1. we want to design 5 feather type flag specs
450*1620 mm
shape and image of flag inserted with material
2. Takeaway Menu update
3. Improving layout and redesisgning function menu with packages
4. Improving layout and redsigning of takeaway catering packages

notes

you can use pictures from from restaurant menu or the building pics as available from our restaurant or any better ideas you have

```html
<!DOCTYPE html>
<html lang="en">
<head>
<meta charset="utf-8">
<title>Spice Lane – Feather Flag Set</title>
<link href="https://fonts.googleapis.com/css2?family=Jost:wght@500;600;700&display=swap" rel="stylesheet">
<style>
  :root {
    --orange: #f29a2e;
    --green: #1f8a3d;
    --ink: #1d1d1f;
    --paper: #ececf0;
    --paper-light: #f5f5f8;
    --white: #ffffff;
    --mint: #d6efe2;
  }
  * { margin: 0; padding: 0; box-sizing: border-box; }
  html, body { width: 729px; height: 1200px; overflow: hidden; background: var(--white); }
  body { font-family: "Jost", sans-serif; color: var(--ink); }

  .canvas {
    position: relative;
    width: 729px;
    height: 1200px;
    background: var(--white);
    overflow: hidden;
  }
  .flag-row {
    position: absolute;
    top: 303px;
    left: 16px;
    display: flex;
    gap: 12px;
  }
  .flag {
    position: relative;
    width: 165px;
    height: 594px;
    background: linear-gradient(180deg, var(--paper) 0%, var(--paper-light) 60%, var(--paper) 100%);
    box-shadow: 1px 2px 4px rgba(0,0,0,.18);
    overflow: hidden;
  }
  .layer { position: absolute; left: 0; right: 0; }
  .text {
    position: absolute; left: 0; right: 0;
    text-align: center; line-height: 1; text-transform: uppercase;
    font-weight: 600;
  }
  .brand {
    position: absolute; left: 0; right: 0;
    text-align: center; line-height: 1;
    font-family: "Jost", sans-serif;
    font-weight: 500; font-size: 18px; color: var(--ink);
  }
  .orange { color: var(--orange); }
  .green { color: var(--green); }
  .white { color: var(--white); }
  .photo { position: absolute; left: 0; right: 0; }

  /* Hours flag */
  .band-orange { background: var(--orange); }
  .band-white { background: var(--white); }
  .band-green { background: var(--green); }

  /* Christmas flag */
  .greeting-panel { background: var(--white); }
</style>
</head>
<body>
<div class="canvas">
  <div class="flag-row">

    <!-- Opening hours flag -->
    <section class="flag flag--hours">
      <div class="brand" style="top:92px;">Spice Lane</div>

      <div class="layer band-orange" style="top:136px;height:51px;"></div>
      <div class="text white" style="top:141px;font-size:24px;">Breakfast</div>
      <div class="text white" style="top:166px;font-size:12px;">(9am–11am)</div>

      <div class="layer band-white" style="top:187px;height:44px;"></div>
      <div class="text green" style="top:190px;font-size:24px;">Lunch</div>
      <div class="text green" style="top:214px;font-size:12px;">(11.30am – 3.00pm)</div>

      <div class="layer band-green" style="top:231px;height:51px;"></div>
      <div class="text white" style="top:236px;font-size:24px;">Dinner</div>
      <div class="text white" style="top:262px;font-size:12px;">(5pm – 10pm)</div>

      <div class="photo" role="img" aria-label="Indian dishes: fried snacks, wraps, kachori with chutney and stuffed paratha"
           style="top:282px;height:188px;background:radial-gradient(ellipse at 50% 50%, #d9a45a 0%, #e8c99a 35%, var(--mint) 75%, var(--paper-light) 100%);"></div>

      <svg class="layer" style="top:482px;" width="165" height="112" viewBox="0 0 165 112" aria-hidden="true">
        <path d="M0 10 L165 4 L165 94 L0 98 Z" fill="var(--green)"/>
      </svg>
      <div class="text white" style="top:531px;font-size:24px;">Open for</div>
    </section>

    <!-- Happy hours flag -->
    <section class="flag flag--drinks">
      <div class="layer band-green" style="top:0;height:26px;"></div>
      <div class="brand" style="top:92px;">Spice Lane</div>

      <div class="text orange" style="top:141px;font-size:13px;">Happy Hours</div>
      <div class="text green" style="top:156px;font-size:22px;">All Drinks</div>
      <div class="text" style="top:181px;font-size:23px;">$5.00</div>
      <div class="text orange" style="top:232px;font-size:12.5px;">Monday to Friday</div>
      <div class="text" style="top:248px;font-size:12px;">(5pm – 7pm)</div>

      <svg class="layer" style="top:286px;" width="165" height="70" viewBox="0 0 165 70" aria-hidden="true">
        <path d="M0 10 Q82 -4 165 8 L165 66 Q82 74 0 62 Z" fill="var(--orange)"/>
      </svg>
      <div class="photo" role="img" aria-label="Three colourful cocktails with lime and fruit garnish"
           style="top:292px;height:84px;left:22px;right:22px;background:linear-gradient(90deg,#f0623a 0%,#f6c13d 25%,#6fbf4a 50%,#e85a5f 80%,#f7d9d9 100%);border-radius:6px;"></div>

      <div class="text" style="top:426px;font-size:19px;">Add a</div>
      <div class="text green" style="top:446px;font-size:27px;">Canape’</div>
      <div class="text" style="top:478px;font-size:15px;">For just</div>
      <div class="text orange" style="top:497px;font-size:30px;">$6.50</div>

      <div class="layer" style="bottom:0;height:60px;background:linear-gradient(180deg,rgba(214,239,226,0),var(--mint));"></div>
    </section>

    <!-- Special lunch flag -->
    <section class="flag flag--lunch">
      <div class="layer band-green" style="top:0;height:26px;"></div>
      <div class="brand" style="top:92px;">Spice Lane</div>

      <div class="text" style="top:143px;font-size:25px;">Special</div>
      <div class="text green" style="top:166px;font-size:37px;">Lunch</div>
      <div class="text orange" style="top:212px;font-size:32px;">$14.90</div>
      <div class="text" style="top:250px;font-size:13px;">(Veg &amp; Non Veg)</div>

      <div class="photo" role="img" aria-label="Kachori with chutney and stuffed paratha with raita and pickle"
           style="top:292px;height:180px;background:radial-gradient(ellipse at 55% 55%, #d9a45a 0%, #ead0a4 35%, var(--mint) 72%, var(--paper-light) 100%);"></div>

      <svg class="layer" style="top:494px;" width="165" height="66" viewBox="0 0 165 66" aria-hidden="true">
        <path d="M0 6 Q82 0 165 4 L165 58 Q82 64 0 60 Z" fill="var(--orange)"/>
      </svg>
      <div class="text" style="top:508px;font-size:11px;letter-spacing:2px;">Available</div>
      <div class="text" style="top:521px;font-size:19px;">Curry &amp; Rice</div>
      <div class="layer band-white" style="top:556px;height:38px;"></div>
    </section>

    <!-- Seasonal greetings flag -->
    <section class="flag flag--christmas">
      <div class="photo" role="img" aria-label="Hanging silver baubles and gold stars"
           style="top:0;height:170px;background:linear-gradient(180deg,#e4e4ea 0%,var(--paper-light) 100%);"></div>
      <div class="brand" style="top:130px;">Spice Lane</div>

      <div class="layer greeting-panel" style="top:172px;height:81px;"></div>
      <div class="text" style="top:182px;font-size:23px;">Merry</div>
      <div class="text orange" style="top:203px;font-size:23px;">Christmas</div>
      <div class="text" style="top:226px;font-size:13.5px;">A Happy New Year</div>

      <div class="photo" role="img" aria-label="Kachori, stuffed paratha and wraps on green and orange brush strokes"
           style="top:253px;height:306px;background:radial-gradient(ellipse at 60% 35%, #d9a45a 0%, #ead0a4 28%, var(--mint) 55%, var(--paper-light) 85%);"></div>
      <div class="photo" role="img" aria-label="Red baubles on pine branches"
           style="top:559px;height:35px;background:linear-gradient(180deg,#3f7d3a 0%,#1f5a2a 100%);"></div>
    </section>

  </div>
</div>
</body>
</html>
```